NEW Website DESIGN for Brightfold Panes & Worktops Company

Brand New website, contemporary, clean, visual (images), not busy. ATTACHED IS OUR LOG THAT YOU MUST USE.

The company is called Brightfold Panes & Worktops (BrightfoldPW)
www.brightfoldpw.com
The website should be www.brightfoldpnw.com
one page for glass one page for solid surfaces www.brightfoldpanesplashes.co.uk
www.brightfoldpanesworktops.co.uk

Target Market(s)

Hotels, Commercial projects, Small focus on residential

Industry/Entity Type

Construction

Number of Pages Required

5+ page

Font styles to use
Sans Serif

Requirements
Must have
• COLOURS AS PER OUR LOGO - WHITE/YELLOW/GREY - WHITE BACK GROUND
• CLEAR SIMPLE NAVIGATION - MODER CLEAN CUT - DESIGN FEEL
• LATEST NAVIGATION FOR IMAGES and text to include per project details
• WORK/PROJECT AREA - NEWS AREA - TEAM AREA/ABOUT US/CONTACT US
• NEW PAGEwww.brightfoldpanesplashes.co.uk - NEW PAGE www.brightfoldpanesworktops.co.uk
• PLEASE COPY THIS TYPE OF TEMPALTE
• https://www.velmarbuild.co.uk/project/grand-suites/
• MOBILE READY
• WORDPRESS
• MODERN IMAGES INCLUDING LUMERAX HALVERN AND GLASS PROJECTS
Nice to have
• NEW DESIGN MODER FRESH
• WEBSITES I LIKE THE TEMPLATE SHOULD BE LIKE THE WEBSITE BELOW
• https://www.velmarbuild.co.uk/
Should not have
• NOT Old fashion template, not busy NAVIGATION
• NO BLACK
• NO DARK GREYS
• NOT LOTS OF YELLOW
• RESDENTIAL IMAGES

```html
<!DOCTYPE html>
<html lang="en">
<head>
<meta charset="utf-8">
<title>Brightfold Panes &amp; Worktops – Solid Surfaces</title>
<link href="https://fonts.googleapis.com/css2?family=Lato:wght@400;700&family=Roboto:wght@400;500;700&display=swap" rel="stylesheet">
<style>
:root{
  --white:#ffffff;
  --yellow:#f5ea1c;
  --yellow-line:#ece43a;
  --grey:#8a8a8a;
  --grey-text:#6f6f6f;
  --ink:#2e2e2e;
  --line:#e6e6e6;
  --footer:#8c8c8c;
}
*{margin:0;padding:0;box-sizing:border-box}
html,body{width:1200px;height:2517px;overflow:hidden;background:var(--white)}
body{position:relative;font-family:"Lato",sans-serif;color:var(--ink)}
.site-header{position:absolute;left:0;top:0;width:1200px;height:141px}
.brand{position:absolute;left:34px;top:20px;width:268px;height:173px;z-index:3}
.brand-shape{position:absolute;left:0;top:114px;width:268px;height:59px;background:var(--white);border-radius:0 0 60% 50%/0 0 100% 100%}
.brand-dot{position:absolute;left:80px;top:0;width:94px;height:94px;border-radius:50%;background:var(--grey)}
.brand-name{position:absolute;left:0;top:110px;width:268px;text-align:center;font-family:"Roboto",sans-serif;font-weight:500;font-size:19px;color:var(--grey)}
.main-nav{position:absolute;top:52px;left:440px;display:flex;height:40px;align-items:center}
.main-nav a{font-family:"Roboto",sans-serif;font-size:13px;font-weight:500;color:var(--ink);text-decoration:none;padding:0 21px;height:64px;display:flex;align-items:center;border-left:1px solid var(--line)}
.main-nav a:first-child{border-left:none}
.main-nav a.is-active{background:var(--yellow);height:39px;margin:0 6px;padding:0 21px;border-left:none}
.hero{position:absolute;left:35px;top:141px;width:1130px;height:483px;background:linear-gradient(100deg,#3b3835 0%,#6b6560 30%,#d8d3c8 50%,#b8aa86 62%,#8a8680 80%,#a5a29c 100%)}
.feature{position:absolute;width:440px}
.feature h2{font-family:"Roboto",sans-serif;font-weight:500;font-size:16px;color:#555;margin-bottom:8px}
.feature p{font-size:12.5px;line-height:21px;margin-bottom:8px}
.feature ul{list-style:none}
.feature li{font-size:12.5px;line-height:29px;padding-left:26px;position:relative}
.feature li svg{position:absolute;left:0;top:10px}
.photo{position:absolute;width:437px;height:269px;border-radius:8px}
.photo-a{background:linear-gradient(160deg,#f4f4f2,#d9dadb 60%,#bfc0c0)}
.photo-b{background:linear-gradient(160deg,#8d8780,#b5a58a 50%,#5e564c)}
.photo-c{background:linear-gradient(170deg,#f1f1ef,#d9d7d3 50%,#9a6a4e 65%,#dcdcdc)}
.photo-d{background:linear-gradient(170deg,#e9e6e1,#d5d2cc 40%,#5a5fc0 60%,#a07a64)}
.contact{position:absolute;left:0;top:2136px;width:1200px}
.contact-rule{position:absolute;left:512px;top:0;width:117px;height:2px;background:var(--yellow-line)}
.contact h2{position:absolute;left:0;top:18px;width:1200px;text-align:center;font-family:"Roboto",sans-serif;font-weight:500;font-size:26px;color:var(--grey-text)}
.card{position:absolute;top:77px;width:289px;height:185px;border:1px solid var(--line);text-align:center}
.card svg{margin-top:36px}
.card h3{font-family:"Roboto",sans-serif;font-weight:500;font-size:16px;letter-spacing:1px;margin-top:6px}
.card p{font-size:12.5px;line-height:16px;margin-top:4px}
.site-footer{position:absolute;left:0;top:2473px;width:1200px;height:44px;background:var(--footer);color:var(--white);font-size:11px}
.site-footer .copy{position:absolute;left:143px;top:15px}
.social{position:absolute;right:143px;top:16px;display:flex;gap:14px}
.social span{width:11px;height:11px;border-radius:50%;background:var(--white)}
</style>
</head>
<body>
<header class="site-header">
  <div class="brand">
    <div class="brand-shape"></div>
    <div class="brand-dot"></div>
    <div class="brand-name">Brightfold Panes &amp; Worktops</div>
  </div>
  <nav class="main-nav">
    <a href="#">Home</a><a href="#">About Us</a><a href="#">Glass</a><a href="#" class="is-active">Solid Surfaces</a><a href="#">Projects</a><a href="#">News</a><a href="#">Contact Us</a>
  </nav>
</header>

<div class="hero" role="img" aria-label="Hotel lobby with a white solid-surface reception desk"></div>

<section class="feature" style="left:143px;top:745px">
  <h2>Lorem ipsum dolor sit amet consectetuer</h2>
  <p>Lorem ipsum dolor sit amet, consectetuer adipiscing elit, sed diam nonummy nibh euismod tincidunt ut laoreet dolore magna aliquam erat volutpat.</p>
  <ul>
    <li><svg width="16" height="12" viewBox="0 0 16 12"><path d="M1 6l5 5L15 1" fill="none" stroke="#e8d91a" stroke-width="1.6"/></svg>Lorem ipsum dolor sit amet, consectetuer adipiscing sed diam nonummy.</li>
    <li><svg width="16" height="12" viewBox="0 0 16 12"><path d="M1 6l5 5L15 1" fill="none" stroke="#e8d91a" stroke-width="1.6"/></svg>Lorem ipsum dolor sit amet adipiscing elit, sed diam nonummy.</li>
    <li><svg width="16" height="12" viewBox="0 0 16 12"><path d="M1 6l5 5L15 1" fill="none" stroke="#e8d91a" stroke-width="1.6"/></svg>Lorem ipsum dolor sit amet adipiscing elit, sed diam d augue feugait nulla.</li>
    <li><svg width="16" height="12" viewBox="0 0 16 12"><path d="M1 6l5 5L15 1" fill="none" stroke="#e8d91a" stroke-width="1.6"/></svg>Lorem ipsum dolor consectetuer adipiscing elit sed diam nonummy.</li>
  </ul>
</section>
<div class="photo photo-a" style="left:622px;top:703px" role="img" aria-label="Curved white reception counter in a bright office foyer"></div>

<div class="photo photo-b" style="left:141px;top:1054px" role="img" aria-label="Timber-clad reception desk in a hotel corridor"></div>
<section class="feature" style="left:618px;top:1097px">
  <h2>Lorem ipsum dolor sit amet consectetuer</h2>
  <p>Lorem ipsum dolor sit amet, consectetuer adipiscing elit, sed diam nonummy nibh euismod tincidunt ut laoreet dolore magna aliquam erat volutpat.</p>
  <ul>
    <li><svg width="16" height="12" viewBox="0 0 16 12"><path d="M1 6l5 5L15 1" fill="none" stroke="#e8d91a" stroke-width="1.6"/></svg>Lorem ipsum dolor sit amet, consectetuer adipiscing sed diam nonummy.</li>
    <li><svg width="16" height="12" viewBox="0 0 16 12"><path d="M1 6l5 5L15 1" fill="none" stroke="#e8d91a" stroke-width="1.6"/></svg>Lorem ipsum dolor sit amet adipiscing elit, sed diam nonummy.</li>
    <li><svg width="16" height="12" viewBox="0 0 16 12"><path d="M1 6l5 5L15 1" fill="none" stroke="#e8d91a" stroke-width="1.6"/></svg>Lorem ipsum dolor sit amet adipiscing elit, sed diam d augue feugait nulla.</li>
    <li><svg width="16" height="12" viewBox="0 0 16 12"><path d="M1 6l5 5L15 1" fill="none" stroke="#e8d91a" stroke-width="1.6"/></svg>Lorem ipsum dolor consectetuer adipiscing elit sed diam nonummy.</li>
  </ul>
</section>

<section class="feature" style="left:143px;top:1447px">
  <h2>Lorem ipsum dolor sit amet consectetuer</h2>
  <p>Lorem ipsum dolor sit amet, consectetuer adipiscing elit, sed diam nonummy nibh euismod tincidunt ut laoreet dolore magna aliquam erat volutpat.</p>
  <ul>
    <li><svg width="16" height="12" viewBox="0 0 16 12"><path d="M1 6l5 5L15 1" fill="none" stroke="#e8d91a" stroke-width="1.6"/></svg>Lorem ipsum dolor sit amet, consectetuer adipiscing sed diam nonummy.</li>
    <li><svg width="16" height="12" viewBox="0 0 16 12"><path d="M1 6l5 5L15 1" fill="none" stroke="#e8d91a" stroke-width="1.6"/></svg>Lorem ipsum dolor sit amet adipiscing elit, sed diam nonummy.</li>
    <li><svg width="16" height="12" viewBox="0 0 16 12"><path d="M1 6l5 5L15 1" fill="none" stroke="#e8d91a" stroke-width="1.6"/></svg>Lorem ipsum dolor sit amet adipiscing elit, sed diam d augue feugait nulla.</li>
    <li><svg width="16" height="12" viewBox="0 0 16 12"><path d="M1 6l5 5L15 1" fill="none" stroke="#e8d91a" stroke-width="1.6"/></svg>Lorem ipsum dolor consectetuer adipiscing elit sed diam nonummy.</li>
  </ul>
</section>
<div class="photo photo-c" style="left:622px;top:1405px" role="img" aria-label="Open white lobby with flowing ceiling and wood-panelled reception"></div>

<div class="photo photo-d" style="left:141px;top:1755px" role="img" aria-label="Round white reception desk beside a lit aquarium wall"></div>
<section class="feature" style="left:618px;top:1798px">
  <h2>Lorem ipsum dolor sit amet consectetuer</h2>
  <p>Lorem ipsum dolor sit amet, consectetuer adipiscing elit, sed diam nonummy nibh euismod tincidunt ut laoreet dolore magna aliquam erat volutpat.</p>
  <ul>
    <li><svg width="16" height="12" viewBox="0 0 16 12"><path d="M1 6l5 5L15 1" fill="none" stroke="#e8d91a" stroke-width="1.6"/></svg>Lorem ipsum dolor sit amet, consectetuer adipiscing sed diam nonummy.</li>
    <li><svg width="16" height="12" viewBox="0 0 16 12"><path d="M1 6l5 5L15 1" fill="none" stroke="#e8d91a" stroke-width="1.6"/></svg>Lorem ipsum dolor sit amet adipiscing elit, sed diam nonummy.</li>
    <li><svg width="16" height="12" viewBox="0 0 16 12"><path d="M1 6l5 5L15 1" fill="none" stroke="#e8d91a" stroke-width="1.6"/></svg>Lorem ipsum dolor sit amet adipiscing elit, sed diam d augue feugait nulla.</li>
    <li><svg width="16" height="12" viewBox="0 0 16 12"><path d="M1 6l5 5L15 1" fill="none" stroke="#e8d91a" stroke-width="1.6"/></svg>Lorem ipsum dolor consectetuer adipiscing elit sed diam nonummy.</li>
  </ul>
</section>

<section class="contact">
  <div class="contact-rule"></div>
  <h2>Contact Us</h2>
  <div class="card" style="left:141px">
    <svg width="26" height="32" viewBox="0 0 26 32"><path d="M13 30C13 30 3 18 3 11a10 10 0 0 1 20 0c0 7-10 19-10 19z" fill="none" stroke="#e8d91a" stroke-width="1.6"/><circle cx="13" cy="11" r="3.5" fill="none" stroke="#e8d91a" stroke-width="1.6"/></svg>
    <h3>Address</h3>
    <p>Harlow Point Ltd<br>Meridian Works Centre<br>Fenwick Road,Oxbridge,OX9 2TR</p>
  </div>
  <div class="card" style="left:455px">
    <svg width="32" height="32" viewBox="0 0 32 32"><path d="M7 3l5 6-3 3c2 5 6 9 11 11l3-3 6 5-3 5C14 30 2 18 3 6z" fill="none" stroke="#e8d91a" stroke-width="1.6"/><path d="M19 4a9 9 0 0 1 9 9M19 9a4 4 0 0 1 4 4" fill="none" stroke="#e8d91a" stroke-width="1.6"/></svg>
    <h3>Call Us</h3>
    <p>+ 44 (0)1632 960418</p>
  </div>
  <div class="card" style="left:769px">
    <svg width="42" height="32" viewBox="0 0 42 32"><rect x="2" y="3" width="38" height="26" fill="none" stroke="#e8d91a" stroke-width="1.6"/><path d="M2 3l19 15L40 3M2 29l14-13M40 29L26 16" fill="none" stroke="#e8d91a" stroke-width="1.6"/></svg>
    <h3>Mail Us</h3>
    <p>info@harlowpoint.com</p>
  </div>
</section>

<footer class="site-footer">
  <span class="copy">Copyright © 2018 Brightfold Panes &amp; Worktops. All Rights Reserved.</span>
  <div class="social"><span></span><span></span><span></span><span></span></div>
</footer>
</body>
</html>
```